Need a new office flyer

I would like an 8.5 x 11" flyer made that can be emailed or printed out and handed to potential customers.  The flyer should include our existing logo and continuity of branding.   I am a commercial real estate broker and market myself to business with 5-50 employee's that are looking to buy or lease space to run their business from.  I focus my efforts on office & warehouse space. The flyer should have a banner "need a new location "
"VLD commercial real estate specializes in helping business and professionals buy/sell or lease  the best spaces for their business.  Take the stress & time out of finding the best location for your business and negotiating a great deal  VLD will do it for you and the best part our service is free to you. Working with VLD is easy as 1, 2, 3
1. Call, Text, Email us today and let us know what your looking to do.
2. VLD  will prepare a list of all the best available spaces that meet your specifications and set up tours of your favorites.
3. We will negotiate the best terms for your space. and help you with all the  details of getting your new space ready for you.
Don't forget the that our services are free to Buyers and Tenants so don't waste your companies time searching for locations, we already know where they are!
Contact us today!
Dale Norcutt
DRE 07354128
VLD Commercial Real Estate
555-317-4829
d.norcutt@vldprop-example.com

```html
<!DOCTYPE html>
<html lang="en">
<head>
<meta charset="UTF-8">
<title>VLD Commercial Real Estate – Need a New Location</title>
<link href="https://fonts.googleapis.com/css2?family=Lato:wght@400;700;900&family=Oswald:wght@300;500;700&display=swap" rel="stylesheet">
<style>
  :root {
    --blue: #2a6aa8;
    --blue-deep: #1f4f86;
    --grey: #8a8f96;
    --ink: #2b2f35;
    --paper: #ffffff;
    --tint: #f3f5f8;
    --backdrop: #e6e8eb;
  }
  * { box-sizing: border-box; margin: 0; padding: 0; }
  html, body { width: 1200px; height: 1200px; overflow: hidden; }
  body { background: var(--backdrop); font-family: "Lato", sans-serif; color: var(--ink); position: relative; }

  .flyer {
    position: absolute; left: 160px; top: 30px;
    width: 880px; height: 1140px;
    background: var(--paper);
    overflow: hidden;
    box-shadow: 0 10px 30px rgba(0,0,0,.18);
  }
  .flyer-shapes { position: absolute; inset: 0; }

  .brand { position: absolute; left: 52px; top: 44px; display: flex; align-items: center; gap: 14px; }
  .brand-dot { width: 64px; height: 64px; border-radius: 50%; background: var(--blue); }
  .brand-name { color: var(--blue); font-weight: 900; line-height: 1; }
  .brand-name .big { display: block; font-size: 58px; letter-spacing: 1px; }
  .brand-name .small { display: block; font-size: 13px; letter-spacing: 4px; text-transform: uppercase; margin-top: 4px; }

  .headline { position: absolute; left: 60px; top: 250px; color: #fff; font-family: "Oswald", sans-serif; text-transform: uppercase; line-height: .95; }
  .headline .thin { display: block; font-weight: 300; font-size: 80px; letter-spacing: -1px; }
  .headline .bold { display: block; font-weight: 700; font-size: 96px; letter-spacing: -1px; }

  .intro { position: absolute; left: 50px; top: 560px; width: 390px; font-size: 14px; line-height: 1.38; }
  .intro p + p { margin-top: 10px; }

  .easy { position: absolute; left: 470px; top: 562px; padding-left: 26px; border-left: 3px solid var(--blue); font-weight: 900; font-size: 32px; line-height: 1.15; color: var(--blue); }
  .easy .lead { color: var(--grey); }

  .steps { position: absolute; left: 0; top: 810px; width: 880px; height: 175px; display: flex; }
  .step { flex: 1; position: relative; text-align: center; color: #fff; font-size: 14px; line-height: 1.4; padding: 78px 28px 0; }
  .step + .step { border-left: 2px dashed rgba(255,255,255,.7); }
  .step-icon { position: absolute; left: 50%; top: -56px; transform: translateX(-50%); width: 120px; height: 120px; border-radius: 50%; background: #fff; border: 5px solid var(--blue); display: flex; align-items: center; justify-content: center; }
  .step-icon svg { width: 60px; height: 60px; }

  .note { position: absolute; left: 60px; top: 995px; width: 760px; text-align: center; font-size: 16px; line-height: 1.38; }
  .note strong { color: var(--blue); font-weight: 900; }
  .rule { position: absolute; left: 50px; right: 50px; top: 1048px; height: 2px; background: var(--blue); }

  .contact { position: absolute; left: 50px; right: 40px; top: 1058px; display: flex; align-items: flex-start; gap: 24px; }
  .cta { font-family: "Oswald", sans-serif; text-transform: uppercase; line-height: .9; color: var(--ink); }
  .cta .thin { display: block; font-weight: 300; font-size: 30px; }
  .cta .bold { display: block; font-weight: 700; font-size: 42px; color: var(--blue); }
  .agent-name { font-weight: 900; font-size: 30px; color: var(--blue); text-transform: uppercase; line-height: 1; }
  .agent-licence { font-size: 15px; margin-top: 2px; }
  .agent-web { display: inline-block; margin-top: 6px; background: var(--blue); color: #fff; font-size: 13px; letter-spacing: 2px; padding: 3px 8px; }
  .reach { margin-left: auto; display: flex; gap: 10px; align-items: flex-start; }
  .reach svg { width: 26px; height: 44px; margin-top: 4px; }
  .reach-phone { font-weight: 900; font-size: 40px; color: var(--blue); line-height: 1; }
  .reach-mail { font-size: 20px; margin-top: 6px; }
</style>
</head>
<body>
<main class="flyer">
  <svg class="flyer-shapes" width="880" height="1140" viewBox="0 0 880 1140">
    <defs>
      <linearGradient id="bandFade" x1="0" x2="1">
        <stop offset="0" stop-color="#2a6aa8" stop-opacity=".75"/>
        <stop offset=".35" stop-color="#2a6aa8"/>
        <stop offset="1" stop-color="#2a6aa8"/>
      </linearGradient>
      <linearGradient id="sky" x1="0" y1="0" x2="1" y2="1">
        <stop offset="0" stop-color="#d7e9f8"/>
        <stop offset=".55" stop-color="#3f87c9"/>
        <stop offset="1" stop-color="#6e9a6a"/>
      </linearGradient>
      <clipPath id="photoClip"><circle cx="680" cy="290" r="190"/></clipPath>
    </defs>
    <polygon class="banner" points="0,230 600,140 660,140 600,470 0,545" fill="#2a6aa8"/>
    <rect x="0" y="545" width="880" height="265" fill="#f3f5f8"/>
    <rect x="0" y="810" width="880" height="175" fill="url(#bandFade)"/>
    <circle cx="680" cy="290" r="202" fill="#fff" stroke="#9aa0a6" stroke-width="6"/>
    <rect role="img" aria-label="Photo of a modern glass office building under a blue sky" x="490" y="100" width="380" height="380" fill="url(#sky)" clip-path="url(#photoClip)"/>
    <path d="M 480 140 A 232 232 0 0 1 880 170" fill="none" stroke="#2a6aa8" stroke-width="12" stroke-linecap="round"/>
    <path d="M 880 420 A 232 232 0 0 1 730 515" fill="none" stroke="#2a6aa8" stroke-width="9" stroke-linecap="round"/>
  </svg>

  <div class="brand">
    <span class="brand-dot"></span>
    <span class="brand-name"><span class="big">VLD</span><span class="small">Commercial Real Estate</span></span>
  </div>

  <h1 class="headline"><span class="thin">Need a new</span><span class="bold">Location</span></h1>

  <section class="intro">
    <p>VLD commercial real estate specializes in helping business and professionals buy/sell or lease the best spaces for their business.</p>
    <p>Take the stress &amp; time out of finding the best location for your business and negotiating a great deal VLD will do it for you and the best part our service is free to you.</p>
  </section>

  <h2 class="easy"><span class="lead">Working</span><br>with VLD is easy<br>as 1, 2, 3</h2>

  <section class="steps">
    <div class="step">
      <div class="step-icon">
        <svg viewBox="0 0 64 64" fill="none" stroke="#2a6aa8" stroke-width="4" stroke-linejoin="round"><rect x="18" y="4" width="30" height="54" rx="5"/><circle cx="33" cy="51" r="2" fill="#2a6aa8"/><rect x="8" y="22" width="30" height="20" rx="2" fill="#fff"/><path d="M8 22 L23 34 L38 22"/></svg>
      </div>
      Call, Text, Email us today and let us know what your looking to do.
    </div>
    <div class="step">
      <div class="step-icon">
        <svg viewBox="0 0 64 64" fill="none" stroke="#2a6aa8" stroke-width="4" stroke-linecap="round" stroke-linejoin="round"><rect x="12" y="8" width="40" height="52" rx="4"/><rect x="24" y="4" width="16" height="8" rx="2" fill="#fff"/><path d="M19 24l3 3 5-5M19 36l3 3 5-5M19 48l3 3 5-5M32 25h13M32 37h13M32 49h13"/></svg>
      </div>
      VLD will prepare a list of all the best available spaces that meet your specifications and set up tours of your favorites.
    </div>
    <div class="step">
      <div class="step-icon">
        <svg viewBox="0 0 64 64" fill="none" stroke="#2a6aa8" stroke-width="4"><rect x="8" y="6" width="48" height="54"/><path d="M8 18h48M8 30h48M20 6v24M32 6v24M44 6v24"/><rect x="24" y="40" width="16" height="20"/><path d="M32 40v20"/></svg>
      </div>
      We will negotiate the best terms for your space. and help you with all the details of getting your new space ready for you.
    </div>
  </section>

  <p class="note">Don't forget the that our services <strong>are free to Buyers and Tenants</strong> so don't waste your companies time searching for locations, we already know where they are!</p>
  <div class="rule"></div>

  <footer class="contact">
    <div class="cta"><span class="thin">Contact us</span><span class="bold">Today!</span></div>
    <div class="agent">
      <div class="agent-name">Dale Norcutt</div>
      <div class="agent-licence">DRE 07354128</div>
      <div class="agent-web">www.vldprop-example.com</div>
    </div>
    <div class="reach">
      <svg viewBox="0 0 26 44" fill="none" stroke="#8a8f96" stroke-width="3"><rect x="2" y="2" width="22" height="40" rx="4"/><path d="M10 36h6"/></svg>
      <div>
        <div class="reach-phone">555-317-4829</div>
        <div class="reach-mail">d.norcutt@vldprop-example.com</div>
      </div>
    </div>
  </footer>
</main>
</body>
</html>
```